A3 Menus for new international restaurant in Singapore.

Looking for new A3 menu design for indoor & outdoor (beautiful garden and trees) restaurant that caters for expat and local families. International menu, cool jazz vibe, great for couples and families. Restaurant called Brass Cove Parlour. I have attached some of the logos we use. Will consider black and white or color options. Restaurant located on a hill where there were tin mines many years ago, hence the name and branding. Looking for three menus (1) Dinner (2) Lunch (3) weekend brunch.

Target Market(s)

Families, young couples and professionals.

Industry/Entity Type

Restaurant

Font styles to use
Serif
Sans Serif

Requirements
Must have
• All food layout on one side of A3, one for each attached menu. Also a space for drinks list on the back.
Nice to have
• Use some of the logo material we have attached.
Should not have

```html
<!DOCTYPE html>
<html lang="en">
<head>
<meta charset="utf-8">
<title>Brass Cove Parlour – Lunch Menu</title>
<link href="https://fonts.googleapis.com/css2?family=Libre+Baskerville:wght@400;700&display=swap" rel="stylesheet">
<style>
  :root {
    --ink: #1a1a1a;
    --frame: #231f20;
    --paper: #ffffff;
    --muted: #7a7a7a;
    --band: #f9b2b2;
    --tree: #fbeaa3;
    --weed: #d9e8f3;
    --hours-head: #a9c9e6;
    --hours-text: #f8e28f;
  }
  * { box-sizing: border-box; margin: 0; padding: 0; }
  html, body { width: 848px; height: 1200px; overflow: hidden; background: var(--frame); }
  body { font-family: "Libre Baskerville", Georgia, serif; color: var(--ink); }

  .menu { position: relative; width: 848px; height: 1200px; background: var(--frame); overflow: hidden; }
  .paper {
    position: absolute; inset: 0; background: var(--paper);
    clip-path: polygon(22px 12px, 418px 12px, 418px 96px, 822px 96px, 822px 1030px, 432px 1040px, 432px 1170px, 22px 1170px);
  }

  .tree-art {
    position: absolute; left: 270px; top: 200px; width: 540px; height: 520px;
    background: radial-gradient(ellipse at 55% 45%, var(--tree) 0%, rgba(251,234,163,.7) 45%, rgba(255,255,255,0) 72%);
  }
  .weed-art {
    position: absolute; left: 40px; top: 800px; width: 220px; height: 360px;
    background: radial-gradient(ellipse at 50% 70%, var(--weed) 0%, rgba(217,232,243,.5) 50%, rgba(255,255,255,0) 75%);
  }

  .brand {
    position: absolute; left: 42px; top: 28px; width: 260px;
    font-weight: 700; font-size: 50px; line-height: 60px; letter-spacing: 2px; color: var(--ink);
  }

  .page-title {
    position: absolute; left: 430px; top: 14px;
    font-weight: 400; font-size: 40px; color: var(--paper);
  }

  .section-band {
    position: absolute; left: 30px; top: 265px; width: 376px; height: 50px;
    background: var(--band); display: flex; align-items: center; justify-content: space-between;
    padding: 0 22px 0 14px;
  }
  .section-band h2 { font-size: 25px; font-weight: 700; color: #3a1d1d; letter-spacing: .5px; }
  .bowl-icon { width: 58px; height: 40px; border-radius: 0 0 30px 30px; background: #e9d6d6; border: 2px solid var(--ink); }

  .item { position: absolute; width: 362px; }
  .item.left { left: 45px; }
  .item.right { left: 445px; width: 336px; }
  .item .line { display: flex; align-items: baseline; font-weight: 700; font-size: 15.5px; white-space: nowrap; }
  .item .line .leader { flex: 1; border-bottom: 2px dotted var(--ink); margin: 0 4px; transform: translateY(-3px); min-width: 10px; }
  .item .desc { font-weight: 700; font-size: 13.5px; line-height: 20px; color: var(--muted); margin-top: 4px; padding-left: 3px; }
  .item .desc strong { color: var(--ink); }
  .item .desc.inline { display: flex; align-items: baseline; }
  .item .desc.inline .leader { flex: 1; border-bottom: 2px dotted var(--muted); margin: 0 4px; transform: translateY(-3px); }
  .item .desc .price { color: var(--ink); font-size: 15px; white-space: nowrap; }

  .hours {
    position: absolute; left: 432px; top: 1040px; width: 416px; height: 160px;
    text-align: center; padding-top: 5px; font-weight: 700;
  }
  .hours h3 { color: var(--hours-head); font-size: 20px; margin-bottom: 8px; }
  .hours p { color: var(--hours-text); font-size: 20px; line-height: 32px; }
</style>
</head>
<body>
<div class="menu">
  <div class="paper"></div>
  <div class="tree-art" role="img" aria-label="Soft yellow drawing of a large garden tree"></div>
  <div class="weed-art" role="img" aria-label="Faint blue drawing of water plants"></div>

  <div class="brand">BRASS<br>COVE<br>PARLOUR</div>
  <h1 class="page-title">Lunch Menu</h1>

  <div class="section-band">
    <h2>LUNCH</h2>
    <div class="bowl-icon" role="img" aria-label="Small drawing of a bowl"></div>
  </div>

  <div class="item left" style="top:331px"><div class="line" style="font-size:14px">Brass Cove Parlour Muesli and Yoghurt<span class="leader"></span>$9.50</div><div class="desc">with fruit compote</div></div>
  <div class="item left" style="top:389px"><div class="line">Scrambled Eggs<span class="leader"></span>$13.50</div><div class="desc">on sour dough toast, with roast tomato, portobello mushroom and chives</div></div>
  <div class="item left" style="top:467px"><div class="line">Baked Gypsy Eggs<span class="leader"></span>$15.50</div><div class="desc">with rustic napolitano sauce, peas and diced pan-fried potato</div></div>
  <div class="item left" style="top:543px"><div class="line">Russian Salad<span class="leader"></span>$15.50</div><div class="desc">with tuna and smoked salmon, carrots, peas, hardboiled farm eggs and potato with a choice of vinaigrette or mayonnaise dressing</div></div>
  <div class="item left" style="top:633px"><div class="line">Classic Greek Salad<span class="leader"></span>$14.50</div><div class="desc">with cherry tomatoes, feta, kalamata olives, green capsicum &amp; cucumber</div></div>
  <div class="item left" style="top:714px"><div class="line" style="font-size:14.5px">Brass Cove Parlour Garden Salad<span class="leader"></span>$12</div><div class="desc">with mesclun leaves, cherry tomatoes, kalamata olives, shaved parmesan, classic vinaigrette and croutons</div></div>
  <div class="item left" style="top:809px"><div class="line">Arugula Salad<span class="leader"></span>$12</div><div class="desc">with goat’s cheese, hazelnuts and a honey mustard dressing</div></div>
  <div class="item left" style="top:877px"><div class="line">Strigoli<span class="leader"></span>$16</div><div class="desc">with beef ragu bolognese</div></div>
  <div class="item left" style="top:929px"><div class="line">Linguini<span class="leader"></span>$17</div><div class="desc">in a light creamy carbonara sauce, with smoked pancetta</div></div>
  <div class="item left" style="top:990px"><div class="line">Rigatoni<span class="leader"></span>$3</div><div class="desc">with aglio, olio and pepperoncino <strong>$15</strong>, with prawns</div></div>
  <div class="item left" style="top:1067px"><div class="line">Roast Pork Belly Ciabatta<span class="leader"></span>$16</div><div class="desc">with arugula, wholegrain mustard and apple cider sauce, served with fries</div></div>

  <div class="item right" style="top:98px"><div class="line">Roast Beef Ciabatta<span class="leader"></span>$17</div><div class="desc">with cheddar cheese, tomato and lettuce, served with fries</div></div>
  <div class="item right" style="top:175px"><div class="line">Calamari Ciabatta<span class="leader"></span>$16</div><div class="desc">with lettuce, kalamansi aioli, served with fries</div></div>
  <div class="item right" style="top:227px"><div class="line" style="font-size:14px">Brass Cove Parlour Bangers &amp; Mash<span class="leader"></span>$17</div><div class="desc">prime pork sausages, buttery mashed potato covered in onion &amp; cider gravy</div></div>
  <div class="item right" style="top:296px"><div class="line">Beer Battered Fish &amp; Chips<span class="leader"></span>$17</div><div class="desc">with homemade tartar sauce and mushy peas</div></div>
  <div class="item right" style="top:347px"><div class="line">Brass Cove Parlour Burger</div>
    <div class="desc">200gms ground prime beef, in a homemade brioche bun with lettuce, tomato and mayo,</div>
    <div class="desc inline" style="margin-top:0">and a side of fries<span class="leader"></span><span class="price">$20</span></div>
    <div class="desc" style="margin-top:8px">Top it with cheese or bacon</div>
    <div class="desc inline" style="margin-top:0">or both<span class="leader"></span><span class="price">add $2 for each</span></div>
  </div>
  <div class="item right" style="top:488px"><div class="line">Selection of freshly baked cakes and</div><div class="line" style="margin-top:6px">tarts<span class="leader"></span>each $9</div></div>
  <div class="item right" style="top:543px"><div class="line">Ice Cream<span class="leader"></span>per scoop $5</div></div>

  <div class="hours">
    <h3>Opening Hours:</h3>
    <p>Tuesday to Friday&nbsp;&nbsp;10am to 12am</p>
    <p>Saturday and Sunday&nbsp;&nbsp;9am to 12am</p>
    <p>Monday&nbsp;&nbsp;Closed</p>
  </div>
</div>
</body>
</html>
```